Educational Textbook Covern Design for mostly females

Create a textbook cover (will be white spiral) using the Brandguide.pdf attached. This will be a textbook given to mostly age 18-25 year old women so a modern trendy cute type design is wanted.
The book cover is 8.5" x 11" which will be printed in CMYK full bleed.
The name "LoriPQX's Dental Hygiene Academy" must be on the cover somewhere and "LoriPQX" has to be either the same height or larger height than the "Dental Hygiene Academy"

Please no real life photos such as images of dentists, etc. This should be all created art.

The year "2025" should be in the design as well.

IMPORTANT UPDATED 8/4/2024
These designs should not look too childish. This should be a professional textbook for dental professionals. All the current designs have too much cartoon art.

Target Market(s)

18-25 year old females

Industry/Entity Type

Dentistry

Font styles to use
Other font styles liked:
• See brand guide

Colors
A7469A
B969AE
D3A5CF
EDDBEB
F8F0F9
6B429C
8869AF
B7A5CE
E3DAEB
F3F0F8

Requirements
Should not have
• No photos, should be all art

```html
<!DOCTYPE html>
<html lang="en">
<head>
<meta charset="utf-8">
<title>LoriPQX's Dental Hygiene Academy – 2025 Textbook Cover</title>
<link href="https://fonts.googleapis.com/css2?family=Lilita+One&display=swap" rel="stylesheet">
<style>
  :root {
    --backdrop: #d8b2ee;
    --paper: #f3f2f4;
    --purple-deep: #5b3d8f;
    --purple-mid: #6a4f9a;
    --lilac: #c48ae8;
    --sunshine: #e6d44e;
    --white: #ffffff;
  }
  * { margin: 0; padding: 0; box-sizing: border-box; }
  html, body {
    width: 1200px; height: 780px; overflow: hidden;
    background: var(--backdrop);
  }
  .stage {
    width: 1200px; height: 780px;
    display: flex; align-items: center; justify-content: center;
  }
  .cover {
    position: relative;
    width: 556px; height: 720px;
    background: var(--paper);
    overflow: hidden;
    font-family: "Lilita One", "Arial Black", sans-serif;
    color: var(--purple-deep);
  }
  .mascot-art {
    position: absolute;
    left: 96px; top: 18px;
    width: 130px; height: 78px;
    border-radius: 40px 40px 26px 26px;
    background: var(--lilac);
  }
  .dot-field {
    position: absolute; left: 0; top: 0;
    width: 556px; height: 720px;
  }
  .dot--deep { fill: var(--purple-deep); }
  .dot--mid { fill: var(--purple-mid); }
  .dot--lilac { fill: var(--lilac); }
  .dot--sun { fill: var(--sunshine); }
  .title-block {
    position: absolute;
    left: 44px; top: 106px;
    width: 500px;
  }
  .year-pill {
    display: inline-block;
    margin-left: 150px;
    padding: 3px 24px;
    border-radius: 20px;
    background: var(--purple-deep);
    color: var(--white);
    font-size: 22px;
    letter-spacing: 4px;
    line-height: 1.2;
  }
  .brand-name {
    font-weight: 400;
    line-height: 0.9;
    color: var(--purple-deep);
  }
  .brand-name .owner { display: block; font-size: 86px; margin-top: 4px; }
  .brand-name .line-dental { display: block; font-size: 86px; padding-left: 24px; }
  .brand-name .line-hygiene { display: block; font-size: 86px; padding-left: 56px; }
  .brand-name .line-academy {
    display: block;
    font-size: 32px;
    letter-spacing: 16px;
    padding-left: 150px;
    margin-top: 6px;
    line-height: 1;
  }
</style>
</head>
<body>
<main class="stage">
  <section class="cover">
    <div class="mascot-art" role="img" aria-label="Illustrated tooth mascot with round glasses holding a pencil"></div>

    <svg class="dot-field" viewBox="0 0 556 720" xmlns="http://www.w3.org/2000/svg">
      <circle class="dot--deep" cx="-6" cy="440" r="46"/>
      <circle class="dot--sun" cx="100" cy="496" r="46"/>
      <circle class="dot--lilac" cx="-6" cy="552" r="46" role="img" aria-label="Badge illustration of graduate tooth character"/>
      <circle class="dot--lilac" cx="206" cy="552" r="46" role="img" aria-label="Badge illustration of tooth character reading"/>
      <circle class="dot--deep" cx="100" cy="608" r="46" role="img" aria-label="Badge illustration of tooth character with idea bulb"/>
      <circle class="dot--sun" cx="312" cy="608" r="46" role="img" aria-label="Badge illustration of graduate tooth character"/>
      <circle class="dot--sun" cx="-6" cy="664" r="46"/>
      <circle class="dot--lilac" cx="206" cy="664" r="46"/>
      <circle class="dot--mid" cx="418" cy="664" r="46"/>
      <circle class="dot--lilac" cx="100" cy="720" r="46"/>
      <circle class="dot--deep" cx="312" cy="720" r="46" role="img" aria-label="Badge illustration of tooth character with lab flask"/>
      <circle class="dot--lilac" cx="524" cy="720" r="46"/>
    </svg>

    <header class="title-block">
      <span class="year-pill">2025</span>
      <h1 class="brand-name">
        <span class="owner">LORIPQX'S</span>
        <span class="line-dental">Dental</span>
        <span class="line-hygiene">Hygiene</span>
        <span class="line-academy">ACADEMY</span>
      </h1>
    </header>
  </section>
</main>
</body>
</html>
```